Website Name Corvane Tally

I need a website called Corvane Tally:

This site is made for: Asking people to write via Call to Action/Email about their experience regarding procedures in beauty treatments cosmetic, aesthetic and plastic surgery and doctors, clinics and institutes in certain countries/counties/etc – good and bad.
We want to find the 5 best, the 5 worst, the most effective, most ineffective, most expensive, most useless procedures and doctors, clinics, cosmetic institutes. We want to rank them and display the good and the bad, and we want to build a site which will be the base for our future projects in digital marketing for clinics, institutes and doctors. We want to build traffic, want to get data via opt in and of course we want personal opinions to feed a review site.

No complicated website just clear and easy to operate. It has to be catchy though. We are looking for a lot of traffic and we want to generate a lot of data which we want to use for future projects.

attached as word document you will find more details

```html
<!DOCTYPE html>
<html lang="en">
<head>
<meta charset="utf-8">
<title>Corvane Tally</title>
<link rel="stylesheet" href="https://fonts.googleapis.com/css2?family=Playfair+Display:wght@700;800;900&family=Lato:wght@300;400;700;900&family=Montserrat:wght@500;600;700&display=swap">
<style>
:root{
  --backdrop:#232323;
  --white:#ffffff;
  --ink:#1d1d1d;
  --muted:#5a5a5a;
  --rust:#c64524;
  --orange-a:#f0912a;
  --orange-b:#d9531f;
  --pink:#f552b5;
  --star-off:#cfcfcf;
  --footer:#212121;
  --skin-a:#f3ddd0;
  --skin-b:#d9a88f;
}
*{margin:0;padding:0;box-sizing:border-box}
html,body{width:1200px;height:1200px;overflow:hidden;background:var(--backdrop)}
.page{position:absolute;left:371px;top:22px;width:736px;height:1862px;transform:scale(0.6211);transform-origin:0 0;background:var(--white);font-family:'Lato',sans-serif;color:var(--ink);overflow:hidden}
.abs{position:absolute}
.serif{font-family:'Playfair Display',serif}
.caps{font-family:'Montserrat',sans-serif;text-transform:uppercase;letter-spacing:1.2px}

/* nav */
.nav{left:0;top:0;width:736px;height:38px;background:var(--white)}
.logo{font-family:'Montserrat',sans-serif;font-weight:700;font-size:13px;color:var(--ink)}
.nav .logo{left:49px;top:12px}
.nav-link{top:16px;font-size:6px;font-weight:500;color:#333}
.nav-link.active{font-weight:700;color:var(--ink)}
.rate-btn{left:586px;top:0;width:150px;height:38px;background:linear-gradient(90deg,var(--orange-a),var(--orange-b));color:var(--white);font-family:'Montserrat',sans-serif;font-weight:700;font-size:9px;display:flex;align-items:center;padding-left:28px}

/* hero */
.hero-photo{left:0;top:38px;width:736px;height:429px;background:linear-gradient(100deg,#f2f0ee 0%,#ead6c8 35%,#e2b9a0 55%,#5a3a2e 75%,#efe9e6 100%)}
.hero-welcome{left:82px;top:174px;font-size:10px;font-weight:300;color:#333}
.hero-title{left:83px;top:184px;font-size:30px;line-height:31px;font-weight:700;color:#1a1a1a;width:330px}
.hero-text{left:85px;top:257px;font-size:8.4px;line-height:13px;font-weight:300;color:#333;width:310px}
.pill{height:26px;border-radius:13px;color:var(--white);font-size:6.5px;display:flex;align-items:center;justify-content:center;letter-spacing:0.3px}
.pill.pink{left:85px;top:297px;width:97px;background:var(--pink)}
.pill.orange{left:187px;top:297px;width:97px;background:linear-gradient(90deg,var(--orange-a),var(--orange-b))}
.round-arrow{top:348px;width:21px;height:21px;border:1px solid #7a5040;border-radius:50%;display:flex;align-items:center;justify-content:center}
.scroll-down{left:668px;top:262px;transform:rotate(-90deg);font-size:5.5px;letter-spacing:2px;color:#333;font-family:'Montserrat',sans-serif;white-space:nowrap}

/* about */
.about-photo{left:82px;top:492px;width:246px;height:246px;border-radius:50%;background:radial-gradient(circle at 45% 50%,var(--skin-b),var(--skin-a) 55%,#f2f0ee 80%)}
.about-heading{left:368px;top:615px;transform:translate(-50%,-50%) rotate(-90deg);font-size:58px;font-weight:800;white-space:nowrap;color:#111}
.about-lead{left:416px;top:540px;width:240px;font-size:5.6px;line-height:11px;font-weight:700;color:#444}
.about-body{left:416px;top:580px;width:240px;font-size:5.6px;line-height:11px;color:#555}
.pill.touch{left:416px;top:673px;width:97px;height:27px;background:linear-gradient(90deg,var(--orange-a),var(--orange-b));font-family:'Montserrat',sans-serif;letter-spacing:1px;font-size:6px}

/* treatments */
.band{left:0;top:750px}
.arch{top:803px;width:148px;height:155px;border-radius:74px 74px 0 0}
.arch.a{left:82px;background:linear-gradient(180deg,#caa48c,#f1d8c7 45%,#f6e6dc)}
.arch.b{left:292px;background:linear-gradient(180deg,#9a7a66,#eed5c6 40%,#f4e4da)}
.arch.c{left:505px;background:linear-gradient(180deg,#cfd8c6,#6b4b3b 35%,#f1ede8 80%)}
.cat-title{top:966px;font-size:13.5px;line-height:16px;font-weight:700;color:var(--white);width:150px}
.check-list{top:1004px;list-style:none}
.check-list li{display:flex;align-items:center;height:14.5px;font-size:4.8px;color:var(--white);text-transform:uppercase;white-space:nowrap}
.check-list svg{width:7px;height:7px;margin-right:7px;flex:none}

/* ranking */
.rank-title{left:0;width:736px;top:1170px;text-align:center;font-size:23px;font-weight:700;letter-spacing:-0.3px}
.rank-sub{left:0;width:736px;top:1204px;text-align:center;font-size:6.5px;font-weight:300;color:#555}
.rank-card{width:175px;height:75px;background:var(--white);border-radius:6px;box-shadow:0 6px 18px rgba(0,0,0,0.09)}
.stars{position:absolute;left:0;right:0;top:12px;display:flex;justify-content:center;gap:5px}
.stars svg{width:13px;height:13px}
.rank-label{position:absolute;left:0;right:0;top:38px;text-align:center;font-family:'Playfair Display',serif;font-weight:700;font-size:13px;line-height:12px}
.rank-label.small{font-size:9.5px;line-height:12px;top:37px;padding:0 12px}

/* review */
.review-photo{left:0;top:1449px;width:296px;height:286px;background:linear-gradient(110deg,#efeae6 0%,#e4c2ad 40%,#d6a68c 60%,#f2eeeb 100%)}
.review-panel{left:296px;top:1449px;width:440px;height:286px;background:var(--rust)}
.review-title{left:332px;top:1462px;font-size:22px;font-weight:700;color:var(--white)}
.field{border:1px solid rgba(255,255,255,0.85);height:24px;color:var(--white);font-size:5.5px;font-weight:700;padding:9px 0 0 9px}
.submit{left:332px;top:1698px;width:74px;height:20px;background:var(--white);color:#333;font-size:5.5px;font-weight:700;display:flex;align-items:center;justify-content:center}

/* footer */
.footer{left:0;top:1735px;width:736px;height:127px;background:var(--footer)}
.footer .logo{left:0;width:736px;text-align:center;top:20px;color:var(--white)}
.foot-links{left:0;width:736px;top:54px;display:flex;justify-content:center;gap:38px;font-size:5.5px;color:#ddd}
.socials{left:0;width:736px;top:88px;display:flex;justify-content:center;gap:8px}
.socials span{width:12px;height:12px;border-radius:50%;background:#e6e6e6}
.socials span.accent{background:var(--rust)}
.copyright{left:0;width:736px;top:110px;text-align:center;font-size:4.5px;color:#777}
</style>
</head>
<body>
<div class="page">

  <header class="nav abs">
    <div class="logo abs">LOGO HERE</div>
    <span class="nav-link caps abs active" style="left:353px">Home</span>
    <span class="nav-link caps abs" style="left:407px">About</span>
    <span class="nav-link caps abs" style="left:465px">Contact</span>
    <span class="nav-link caps abs" style="left:533px">Dsvgo Site</span>
    <div class="rate-btn abs">RATE &amp; REVIEW</div>
  </header>

  <section>
    <div class="hero-photo abs" role="img" aria-label="Photo of a woman lying on white bedding"></div>
    <p class="hero-welcome abs">Welcome to Corvane Tally</p>
    <h1 class="hero-title serif abs">Lorem ipsum dolor sit amet consectetur.</h1>
    <p class="hero-text abs">Lorem ipsum dolor sit amet consectetur. Facilisi mattis euismod ullamcorper sed. Fames faucibus laoreet vivamus sit massa morbi ut mauris.</p>
    <div class="pill pink abs">KNOW MORE</div>
    <div class="pill orange abs">CONTACT US</div>
    <div class="round-arrow abs" style="left:83px"><svg width="6" height="6" viewBox="0 0 6 6"><path d="M4 1 L2 3 L4 5" fill="none" stroke="#5a3a2e" stroke-width="0.8"/></svg></div>
    <div class="round-arrow abs" style="left:110px"><svg width="6" height="6" viewBox="0 0 6 6"><path d="M2 1 L4 3 L2 5" fill="none" stroke="#5a3a2e" stroke-width="0.8"/></svg></div>
    <div class="scroll-down abs">SCROLL DOWN</div>
    <svg class="abs" style="left:665px;top:205px" width="14" height="100" viewBox="0 0 14 100"><path d="M12 0 V93 L4 86" fill="none" stroke="#444" stroke-width="0.6"/></svg>
  </section>

  <section>
    <div class="about-photo abs" role="img" aria-label="Photo of two smiling women in swimwear sitting together"></div>
    <h2 class="about-heading serif abs">About Us</h2>
    <p class="about-lead abs">Lorem ipsum dolor sit amet consectetur. Aliquam consequat mi sit in. Imperdiet ornare egestas laoreet nam. Nisi cursus at etiam pellentesque enim velit blandit. Dolor eget sit commodo augue molestie arcu.</p>
    <p class="about-body abs">Lorem ipsum dolor sit amet consectetur. Aliquam consequat mi sit in. Imperdiet ornare egestas laoreet nam. Nisi cursus at etiam pellentesque enim velit blandit. Dolor eget sit commodo augue molestie arcu. Cras malesuada libero molestie odio. Amet id magnis quisque accumsan duis. Lacinia suspendisse diam et sodales cursus. A quis interdum nibh dolor tincidunt. Id lectus rutrum ullamcorper ipsum ornare urna integer. Volutpat nulla bibendum commodo id mauris varius sollicitudin. Iaculis viverra tortor vitae fermentum et.</p>
    <div class="pill touch abs">GET IN TOUCH</div>
  </section>

  <section>
    <svg class="band abs" width="736" height="390" viewBox="0 0 736 390">
      <path d="M0 12 C60 4 110 24 170 18 C230 12 280 4 340 12 C400 20 440 22 500 12 C560 4 620 8 680 14 C710 18 730 20 736 20 V364 C700 360 660 350 610 360 C560 370 520 374 470 364 C420 354 380 352 330 362 C280 372 240 374 190 364 C140 354 90 352 40 360 C20 364 8 362 0 360 Z" fill="var(--rust)"/>
    </svg>
    <div class="arch a abs" role="img" aria-label="Photo of a woman touching her forehead"></div>
    <div class="arch b abs" role="img" aria-label="Close-up photo of a woman's face"></div>
    <div class="arch c abs" role="img" aria-label="Photo of a smiling mature woman"></div>

    <h3 class="cat-title serif abs" style="left:82px">Aesthetic Medicine Treatments</h3>
    <h3 class="cat-title serif abs" style="left:292px">Cosmetic Treatments</h3>
    <h3 class="cat-title serif abs" style="left:505px">Aesthetic &amp; Plastic Surgery</h3>

    <svg width="0" height="0" style="position:absolute"><defs><symbol id="tick" viewBox="0 0 10 10"><circle cx="5" cy="5" r="5" fill="#fff"/><path d="M2.8 5.2 L4.4 6.7 L7.3 3.6" fill="none" stroke="var(--rust)" stroke-width="1.3"/></symbol></defs></svg>

    <ul class="check-list abs" style="left:82px">
      <li><svg><use href="#tick"/></svg>Neurelax</li>
      <li><svg><use href="#tick"/></svg>Filler/Hyaluron</li>
      <li><svg><use href="#tick"/></svg>Laser</li>
      <li><svg><use href="#tick"/></svg>Hyperhydrosis/Sweat Glands</li>
      <li><svg><use href="#tick"/></svg>Besenreiser</li>
    </ul>
    <ul class="check-list abs" style="left:198px">
      <li><svg><use href="#tick"/></svg>Stretchmarks</li>
      <li><svg><use href="#tick"/></svg>Threadlift</li>
      <li><svg><use href="#tick"/></svg>Cryolipolysis</li>
      <li><svg><use href="#tick"/></svg>PRP Treatment</li>
      <li><svg><use href="#tick"/></svg>Chemical Peelings</li>
    </ul>
    <ul class="check-list abs" style="left:292px">
      <li><svg><use href="#tick"/></svg>Aqua Jet Infusion</li>
      <li><svg><use href="#tick"/></svg>Microdermabrasion</li>
      <li><svg><use href="#tick"/></svg>Microneedling</li>
      <li><svg><use href="#tick"/></svg>Cold Lifting</li>
    </ul>
    <ul class="check-list abs" style="left:386px">
      <li><svg><use href="#tick"/></svg>Plasma Pen</li>
      <li><svg><use href="#tick"/></svg>Mesotherapie</li>
      <li><svg><use href="#tick"/></svg>Veltrin Deepneedling</li>
    </ul>
    <ul class="check-list abs" style="left:505px">
      <li><svg><use href="#tick"/></svg>Gesicht&amp;Hals</li>
      <li><svg><use href="#tick"/></svg>Körper</li>
      <li><svg><use href="#tick"/></svg>Brust</li>
    </ul>
  </section>

  <section>
    <svg width="0" height="0" style="position:absolute"><defs>
      <symbol id="star" viewBox="0 0 24 24"><path d="M12 1.5 L15.1 8.2 L22.4 8.9 L16.9 13.8 L18.5 21 L12 17.2 L5.5 21 L7.1 13.8 L1.6 8.9 L8.9 8.2 Z"/></symbol>
      <linearGradient id="starGrad" x1="0" y1="0" x2="0" y2="1"><stop offset="0" stop-color="#f08a2a"/><stop offset="1" stop-color="#d04a1e"/></linearGradient>
    </defs></svg>

    <h2 class="rank-title serif abs">RANKING SITE TREATMENTS</h2>
    <p class="rank-sub abs">Where all the incoming reviews are listet as follows</p>

    <div class="rank-card abs" style="left:83px;top:1241px"><div class="stars"><svg fill="var(--star-off)"><use href="#star"/></svg><svg fill="var(--star-off)"><use href="#star"/></svg><svg fill="var(--star-off)"><use href="#star"/></svg><svg fill="var(--star-off)"><use href="#star"/></svg><svg fill="var(--star-off)"><use href="#star"/></svg></div><div class="rank-label">Best</div></div>
    <div class="rank-card abs" style="left:280px;top:1241px"><div class="stars"><svg fill="var(--star-off)"><use href="#star"/></svg><svg fill="var(--star-off)"><use href="#star"/></svg><svg fill="var(--star-off)"><use href="#star"/></svg><svg fill="var(--star-off)"><use href="#star"/></svg><svg fill="var(--star-off)"><use href="#star"/></svg></div><div class="rank-label">Worst</div></div>
    <div class="rank-card abs" style="left:477px;top:1241px"><div class="stars"><svg fill="var(--star-off)"><use href="#star"/></svg><svg fill="var(--star-off)"><use href="#star"/></svg><svg fill="var(--star-off)"><use href="#star"/></svg><svg fill="var(--star-off)"><use href="#star"/></svg><svg fill="var(--star-off)"><use href="#star"/></svg></div><div class="rank-label">Most effective</div></div>
    <div class="rank-card abs" style="left:83px;top:1340px"><div class="stars"><svg fill="var(--star-off)"><use href="#star"/></svg><svg fill="var(--star-off)"><use href="#star"/></svg><svg fill="var(--star-off)"><use href="#star"/></svg><svg fill="var(--star-off)"><use href="#star"/></svg><svg fill="var(--star-off)"><use href="#star"/></svg></div><div class="rank-label">Most ineffective</div></div>
    <div class="rank-card abs" style="left:280px;top:1340px"><div class="stars"><svg fill="url(#starGrad)"><use href="#star"/></svg><svg fill="url(#starGrad)"><use href="#star"/></svg><svg fill="url(#starGrad)"><use href="#star"/></svg><svg fill="url(#starGrad)"><use href="#star"/></svg><svg fill="var(--star-off)"><use href="#star"/></svg></div><div class="rank-label">Most expensive</div></div>
    <div class="rank-card abs" style="left:477px;top:1340px"><div class="stars"><svg fill="var(--star-off)"><use href="#star"/></svg><svg fill="var(--star-off)"><use href="#star"/></svg><svg fill="var(--star-off)"><use href="#star"/></svg><svg fill="var(--star-off)"><use href="#star"/></svg><svg fill="var(--star-off)"><use href="#star"/></svg></div><div class="rank-label small">Most useless TREATMENTS in<br>each of the 3 categories</div></div>
  </section>

  <section>
    <div class="review-photo abs" role="img" aria-label="Photo of a smiling woman lying on white bedding"></div>
    <div class="review-panel abs"></div>
    <h2 class="review-title serif abs">REVIEW SITE</h2>
    <div class="field abs" style="left:332px;top:1506px;width:256px">Name of Reviewer</div>
    <div class="field abs" style="left:332px;top:1538px;width:256px">Region / County</div>
    <div class="field abs" style="left:332px;top:1570px;width:123px">Doctor Name</div>
    <div class="field abs" style="left:464px;top:1570px;width:124px">Clinic</div>
    <div class="field abs" style="left:332px;top:1602px;width:256px">Institute</div>
    <div class="field abs" style="left:332px;top:1634px;width:256px;height:53px">Message</div>
    <div class="submit caps abs">Submit</div>
  </section>

  <footer class="footer abs">
    <div class="logo abs">LOGO HERE</div>
    <nav class="foot-links caps abs"><span>Home</span><span>About</span><span>Contact</span><span>Terms and Conditions</span><span>Privacy &amp; Cookie Polica</span><span>Dsvgo Site</span></nav>
    <div class="socials abs"><span></span><span class="accent"></span><span></span><span></span><span></span><span></span></div>
    <p class="copyright caps abs">Copyright © 2022. All rights reserved.</p>
  </footer>

</div>
</body>
</html>
```